Consumer Facing Energy Data Analytics Startup Needs a Postcard to Promote New Product

We need a set of 2 postcards (6 x 4.25 inches as describers in the attached files) to help us promote our product for a new company based in San Francisco called "Lumo Crest".
We develop an alert platform for customers of energy utility companies. Our initial product is "Lumo Signal" - an application that helps people better manage their energy bill by sending an SMS or email alter in advance of a high bill.
We would like to see designs that use the colors blue and orange (same as in the website: www.lumocrest.example). The text of the postcards will be reworked once a layout has been chosen, but we welcome original ways to attract the customers' attention.
Our goal is ultimately to have our targets go the our website and sign up for our service.
The final deliverable should be 8 vector files (preferable .eps, 4 file types, one version in print and one in web format):
- front of card for our small and medium business customers
- front of card for our residential customers
- back of card for our small and medium business customers
- back of card for our residential customers
- DINPro and Avenir

```html
<!DOCTYPE html>
<html lang="en">
<head>
<meta charset="utf-8">
<title>Lumo Crest – Postcard</title>
<link rel="stylesheet" href="https://fonts.googleapis.com/css2?family=Ubuntu:wght@400;500&display=swap">
<style>
  :root {
    --frame-orange: #f2a73b;
    --accent-orange: #f5a623;
    --brand-blue: #3f8fcf;
    --body-grey: #55595e;
    --paper: #ffffff;
    --page-bg: #e9e9e9;
    --photo-light: #f3e3d6;
    --photo-mid: #dcb9a0;
    --photo-dark: #8d8f95;
  }
  * { margin: 0; padding: 0; box-sizing: border-box; }
  html, body {
    width: 1200px;
    height: 858px;
    overflow: hidden;
    background: var(--page-bg);
  }
  .postcard {
    position: relative;
    width: 1200px;
    height: 858px;
    background: var(--frame-orange);
    padding: 14px;
    font-family: "Ubuntu", sans-serif;
  }
  .card-face {
    position: relative;
    width: 100%;
    height: 100%;
    background: var(--paper);
    border-radius: 6px;
    overflow: hidden;
    box-shadow: inset 0 0 10px rgba(0,0,0,0.12);
  }
  .site-link {
    position: absolute;
    left: 86px;
    top: 100px;
    display: flex;
    align-items: center;
    gap: 12px;
    color: var(--brand-blue);
    font-size: 30px;
    font-weight: 400;
  }
  .site-link svg { width: 26px; height: 26px; }
  .brand-lockup {
    position: absolute;
    left: 560px;
    top: 52px;
    display: flex;
    align-items: center;
    gap: 26px;
  }
  .brand-dot {
    width: 64px;
    height: 64px;
    border-radius: 50%;
    background: var(--accent-orange);
  }
  .brand-name {
    color: var(--brand-blue);
    font-size: 56px;
    font-weight: 400;
    letter-spacing: 5px;
    text-transform: uppercase;
    line-height: 1;
  }
  .hand-with-phone {
    position: absolute;
    left: 70px;
    top: 200px;
    width: 500px;
    height: 600px;
    border-radius: 60px;
    background: linear-gradient(170deg, var(--photo-light) 0%, var(--photo-mid) 55%, var(--photo-dark) 100%);
  }
  .message {
    position: absolute;
    left: 618px;
    top: 250px;
    width: 530px;
    color: var(--body-grey);
    font-size: 30px;
    line-height: 41px;
  }
  .message p + p { margin-top: 18px; text-align: justify; }
  .phone-line {
    position: absolute;
    left: 716px;
    top: 720px;
    display: flex;
    align-items: center;
    gap: 14px;
    color: var(--accent-orange);
    font-size: 35px;
    font-weight: 400;
  }
  .phone-line svg { width: 42px; height: 42px; }
  .footer-band {
    position: absolute;
    right: 0;
    bottom: 0;
    width: 580px;
    height: 14px;
    display: flex;
    flex-direction: column;
  }
  .footer-band .band-blue { flex: 1; background: var(--brand-blue); }
  .footer-band .band-orange { flex: 1; background: var(--accent-orange); }
</style>
</head>
<body>
  <main class="postcard">
    <section class="card-face">
      <div class="site-link">
        <svg viewBox="0 0 24 24" fill="none" stroke="#f5a623" stroke-width="1.8" aria-hidden="true">
          <circle cx="12" cy="12" r="10"/>
          <ellipse cx="12" cy="12" rx="4.5" ry="10"/>
          <line x1="2" y1="12" x2="22" y2="12"/>
          <path d="M4 7h16M4 17h16"/>
        </svg>
        <span>www.lumocrest.example</span>
      </div>

      <div class="brand-lockup">
        <div class="brand-dot" aria-hidden="true"></div>
        <div class="brand-name">Lumo Crest</div>
      </div>

      <div class="hand-with-phone" role="img" aria-label="Photo of a hand holding a smartphone showing a Lumo Signal bill prediction alert"></div>

      <div class="message">
        <p>Lumo Crest helps you predict and avoid your high energy bills.</p>
        <p>Lumo Crest employs advanced analytics software to assess customer energy use on a daily basis. We predict monthly energy bills based on current usage, and provide customer alerts and tips when use is above normal.</p>
      </div>

      <div class="phone-line">
        <svg viewBox="0 0 24 24" aria-hidden="true">
          <circle cx="12" cy="12" r="10.5" fill="none" stroke="#f5a623" stroke-width="1.6"/>
          <path d="M8.6 6.5c.4-.3 1-.3 1.3.1l1.2 1.8c.3.4.2 1-.2 1.3l-.8.6c.5 1.3 1.5 2.5 2.8 3.2l.7-.7c.4-.4 1-.4 1.3 0l1.6 1.4c.4.3.4.9.1 1.3l-.9 1c-.6.6-1.5.8-2.3.5-3-1.2-5.3-3.7-6.3-6.8-.2-.8 0-1.6.6-2.1z" fill="#f5a623"/>
        </svg>
        <span>012-555-0147</span>
      </div>

      <div class="footer-band" aria-hidden="true">
        <div class="band-blue"></div>
        <div class="band-orange"></div>
      </div>
    </section>
  </main>
</body>
</html>
```